Brisbane IT support business needs our first letterhead (Contest)

Hello we are a Brisbane based Information Technology company providing support and services to small and medium sized businesses. We provide a range of services and solutions.

The business name is Kestrel Data Network Systems, or KDNS for short.

I am looking for a letterhead that looks professional (don't we all want that), but most importantly, it most utilize the colours in the logo attached, and any text used preferably in font type: HandelGotDBol.

```html
<!DOCTYPE html>
<html lang="en">
<head>
<meta charset="utf-8">
<title>Kestrel Data Network Systems Letterhead</title>
<link rel="stylesheet" href="https://fonts.googleapis.com/css2?family=EB+Garamond:wght@400&display=swap">
<style>
  :root {
    --orange: #ec7f25;
    --navy: #0f4a63;
    --paper: #ffffff;
    --backdrop: #e9e9e7;
    --ink: #111111;
  }
  html, body {
    margin: 0;
    width: 1200px;
    height: 900px;
    overflow: hidden;
    background: var(--backdrop);
  }
  .letterhead {
    position: absolute;
    left: 310px;
    top: 40px;
    width: 580px;
    height: 820px;
    background: var(--paper);
    box-shadow: 0 2px 8px rgba(0,0,0,0.18);
    overflow: hidden;
  }
  .letterhead__bands {
    position: absolute;
    inset: 0;
  }
  .company-name {
    position: absolute;
    left: 24px;
    top: 112px;
    width: 260px;
    margin: 0;
    font-family: "EB Garamond", serif;
    font-weight: 400;
    font-size: 26px;
    line-height: 28px;
    color: var(--navy);
  }
  .contact {
    position: absolute;
    right: 24px;
    top: 44px;
    margin: 0;
    text-align: right;
    font-family: "EB Garamond", serif;
    font-size: 21px;
    line-height: 22px;
    color: var(--ink);
    font-style: normal;
  }
  .email {
    position: absolute;
    right: 24px;
    bottom: 8px;
    margin: 0;
    font-family: "EB Garamond", serif;
    font-size: 21px;
    color: var(--ink);
  }
</style>
</head>
<body>
  <main class="letterhead">
    <svg class="letterhead__bands" width="580" height="820" viewBox="0 0 580 820">
      <path class="band-top" d="M0,0 H580 V20 C420,14 200,40 0,80 Z" fill="var(--orange)"/>
      <path class="band-bottom" d="M0,820 V772 C180,790 400,770 580,722 V820 Z" fill="var(--orange)"/>
    </svg>

    <p class="company-name">Kestrel Data Network<br>Systems</p>

    <address class="contact">
      Sample Address<br>
      Sample Street<br>
      Tel: 123-555-017<br>
      Fax: 123-555-02
    </address>

    <p class="email">Email: yourname@example.com</p>
  </main>
</body>
</html>
```